3.5" x 11" Door Hanger Design - Residential Roofing Company

We are looking for a double-sided door hanger that we can hang on the doors of prospects. This door hanger would have some brief information about our company, a phone number, website, and then the services that we offer. I don't know that it will have enough room for a lot of pictures, but feel free to use those from the marketing brochure if you think it'll work and I can get you the original as needed.
I have uploaded our certifications, logo, and then our current marketing brochure. The design should be cohesive with our marketing brochure, but doesn't have to match it perfectly.
Lastly, attached is the template that we are planning to print off of. This has a tear off portion at the bottom for a business card for a sales rep. The size of the overall door hanger will be 3.5" x 11", with the bottom 2.5" being the tear off business card with the salesman's information. I'll get you the sales reps information during the final design phase, but we will need name, title, phone number, email, business address, business website, list of services, and then the words "AZ ROC 562071" all on that small portion as well so if they tear it off they still have all the info.

```html
<!DOCTYPE html>
<html lang="en">
<head>
<meta charset="utf-8">
<title>Kestrel Roofing – Door Hanger</title>
<link href="https://fonts.googleapis.com/css2?family=Bitter:wght@700;800&family=Merriweather:wght@700;900&display=swap" rel="stylesheet">
<style>
  :root {
    --stage: #2b2b2b;
    --orange: #e85a21;
    --sky-top: #7eaad9;
    --sky-bottom: #eef2fa;
    --ink: #111111;
    --charcoal: #333333;
    --hole: #5e5e5e;
    --white: #ffffff;
    --seal: #d4d6da;
    --guide-cyan: #1ba1e2;
    --guide-magenta: #e0218a;
  }
  * { margin: 0; padding: 0; box-sizing: border-box; }
  html, body { width: 865px; height: 1200px; overflow: hidden; background: var(--stage); }
  .canvas { position: relative; width: 865px; height: 1200px; }

  .hanger { position: absolute; top: 70px; width: 345px; height: 1060px; overflow: hidden; }
  .hanger--front { left: 75px; background: linear-gradient(to bottom, var(--sky-top) 0, var(--sky-bottom) 480px, var(--sky-bottom) 100%); }
  .hanger--back { left: 445px; background: var(--orange); }

  .shapes { position: absolute; inset: 0; width: 345px; height: 1060px; }

  .house-photo { position: absolute; left: 0; top: 490px; width: 345px; height: 270px;
    background: linear-gradient(160deg, #5f6878 0%, #8d95a4 40%, #4a4f5c 75%, #6d6a5e 100%); }

  .brand-name { position: absolute; left: 0; width: 345px; top: 309px; text-align: center;
    font-family: 'Bitter', serif; font-weight: 800; font-size: 35px; line-height: 1; color: var(--ink); }

  .tagline { position: absolute; left: 0; width: 345px; top: 372px; text-align: center;
    font-family: 'Bitter', serif; font-weight: 800; font-size: 34px; line-height: 32px;
    color: var(--orange); text-shadow: 1px 1px 0 var(--white), -1px -1px 0 var(--white), 1px -1px 0 var(--white), -1px 1px 0 var(--white); }

  .call-now { position: absolute; left: 0; width: 345px; top: 771px; text-align: center;
    font-family: 'Merriweather', serif; font-weight: 900; font-size: 23px; line-height: 1; color: var(--charcoal); }
  .call-phone { position: absolute; left: 0; width: 345px; top: 796px; text-align: center;
    font-family: 'Merriweather', serif; font-weight: 700; font-size: 27px; line-height: 1; color: var(--orange); }

  .service-title { position: absolute; left: 0; width: 345px; text-align: center;
    font-family: 'Merriweather', serif; font-weight: 900; font-size: 14px; line-height: 16px; color: var(--white); }
  .service-photo { position: absolute; left: 50px; width: 244px; border: 1.5px solid var(--white); }
  .photo-seam { background: linear-gradient(170deg, #4d5e45 0%, #9ea0a3 30%, #c9cbcd 60%, #8d9094 100%); }
  .photo-metal { background: linear-gradient(100deg, #a7a9ab 0%, #c7cacc 45%, #d9e0e6 60%, #5a5a5a 100%); }
  .photo-tile { background: linear-gradient(170deg, #5d6c50 0%, #6b7280 35%, #7c7f86 65%, #7a6a55 100%); }
  .photo-tile-system { background: linear-gradient(175deg, #c9ccd2 0%, #5a5e68 40%, #d7dae0 70%, #4b4f58 100%); }
  .photo-shingle { background: linear-gradient(160deg, #6e6e6e 0%, #8a8a8a 40%, #5e5e5e 75%, #7c7c7c 100%); }

  .contact { position: absolute; left: 0; width: 345px; top: 756px; text-align: center;
    font-family: 'Merriweather', serif; font-weight: 700; font-size: 11.5px; line-height: 17px; color: var(--white); }

  .tearoff { position: absolute; left: 0; top: 864px; width: 345px; height: 196px; }
  .tearoff--orange { background: var(--orange); }
  .tearoff--white { background: var(--white); }
  .field-label { position: absolute; left: 34px; font-family: 'Merriweather', serif; font-weight: 900;
    font-size: 11.5px; line-height: 15px; }
  .tearoff--orange .field-label { color: var(--white); }
  .tearoff--white .field-label { color: var(--orange); }
  .field-line { position: absolute; left: 116px; width: 195px; height: 0; border-top: 1px solid; }
  .tearoff--orange .field-line { border-color: var(--white); }
  .tearoff--white .field-line { border-color: var(--orange); }
</style>
</head>
<body>
<div class="canvas">

  <section class="hanger hanger--front">
    <div class="house-photo" role="img" aria-label="Photo of a two-storey house with a dark standing seam metal roof"></div>

    <svg class="shapes" viewBox="0 0 345 1060" aria-hidden="true">
      <polygon points="172,654 345,743 345,864 0,864 0,743" fill="var(--white)"/>
      <polyline points="0,748 172,658 345,748" fill="none" stroke="var(--orange)" stroke-width="11"/>
      <!-- certification seals -->
      <rect x="112" y="708" width="44" height="44" rx="6" fill="var(--seal)"/>
      <rect x="181" y="708" width="44" height="44" rx="6" fill="var(--seal)"/>
      <!-- hanger hole -->
      <polygon points="84,0 110,0 150,58 126,76" fill="var(--hole)"/>
      <circle cx="172" cy="130" r="72" fill="var(--hole)"/>
      <circle cx="172" cy="130" r="78" fill="none" stroke="var(--guide-cyan)" stroke-width="0.8"/>
      <polyline points="82,10 122,72" fill="none" stroke="var(--guide-cyan)" stroke-width="0.8"/>
      <polyline points="124,10 150,50" fill="none" stroke="var(--guide-cyan)" stroke-width="0.8"/>
      <rect x="5" y="5" width="335" height="1050" fill="none" stroke="var(--guide-magenta)" stroke-width="0.6"/>
      <rect x="10" y="10" width="325" height="844" fill="none" stroke="var(--guide-cyan)" stroke-width="0.6"/>
    </svg>

    <div class="brand-name">Kestrel Roofing</div>
    <div class="tagline">Quality Roofing<br>you can trust</div>
    <div class="call-now">CALL NOW</div>
    <div class="call-phone">(555) 014-2290</div>

    <div class="tearoff tearoff--orange">
      <div class="field-label" style="top:28px">NAME</div>
      <div class="field-line" style="top:39px"></div>
      <div class="field-line" style="top:64px"></div>
      <div class="field-label" style="top:79px">TITLE</div>
      <div class="field-line" style="top:88px"></div>
      <div class="field-line" style="top:113px"></div>
      <div class="field-label" style="top:129px">PHONE<br>NUMBER</div>
      <div class="field-line" style="top:137px"></div>
      <div class="field-line" style="top:161px"></div>
      <svg class="shapes" viewBox="0 0 345 196" style="height:196px" aria-hidden="true">
        <rect x="10" y="5" width="325" height="181" fill="none" stroke="var(--guide-cyan)" stroke-width="0.6"/>
      </svg>
    </div>
  </section>

  <section class="hanger hanger--back">
    <svg class="shapes" viewBox="0 0 345 1060" aria-hidden="true">
      <polygon points="235,0 261,0 219,76 195,58" fill="var(--hole)"/>
      <circle cx="172" cy="130" r="72" fill="var(--hole)"/>
      <circle cx="172" cy="130" r="78" fill="none" stroke="var(--guide-cyan)" stroke-width="0.8"/>
      <polyline points="221,10 195,50" fill="none" stroke="var(--guide-cyan)" stroke-width="0.8"/>
      <polyline points="263,10 223,72" fill="none" stroke="var(--guide-cyan)" stroke-width="0.8"/>
      <rect x="5" y="5" width="335" height="850" fill="none" stroke="var(--guide-magenta)" stroke-width="0.6"/>
      <rect x="10" y="10" width="325" height="844" fill="none" stroke="#8a8a8a" stroke-width="0.6"/>
    </svg>

    <div class="service-title" style="top:228px">Standing Seam</div>
    <div class="service-photo photo-seam" style="top:250px;height:74px" role="img" aria-label="Standing seam metal roof with ridge cap"></div>
    <div class="service-title" style="top:331px">Metal</div>
    <div class="service-photo photo-metal" style="top:354px;height:74px" role="img" aria-label="Corrugated metal roof with a skylight"></div>
    <div class="service-title" style="top:434px">Tile</div>
    <div class="service-photo photo-tile" style="top:457px;height:74px" role="img" aria-label="House with a grey tile roof"></div>
    <div class="service-title" style="top:538px">Tile Roofing System</div>
    <div class="service-photo photo-tile-system" style="top:561px;height:75px" role="img" aria-label="Stacks of roof tiles loaded on underlayment"></div>
    <div class="service-title" style="top:645px">Shingle</div>
    <div class="service-photo photo-shingle" style="top:668px;height:81px" role="img" aria-label="Asphalt shingle roof with vent pipes"></div>

    <div class="contact">
      120 Ridge Ave, Cedar Bluff AZ 86000<br>
      (555) 014-2290<br>
      info@kestrel-roofing.com<br>
      Monday-Friday: 8am-5pm<br>
      www.kestrel-roofing.com
    </div>

    <div class="tearoff tearoff--white">
      <div class="field-label" style="top:28px">EMAIL</div>
      <div class="field-line" style="top:39px"></div>
      <div class="field-line" style="top:64px"></div>
      <div class="field-label" style="top:79px">BUSINESS<br>ADDRESS</div>
      <div class="field-line" style="top:88px"></div>
      <div class="field-line" style="top:113px"></div>
      <div class="field-label" style="top:129px">BUSINESS<br>WEBSITE</div>
      <div class="field-line" style="top:137px"></div>
      <div class="field-line" style="top:161px"></div>
    </div>
  </section>

</div>
</body>
</html>
```